Courier Business - Wordpress Design Project

Looking for a designer that can develop a 5 page clean website for a company I have a steak in,

http://parcel-brisk.example.com.au/

is the current website and I looks terrible,

The logo is hosted on the current site

Target Market(s)

Business to Business

Industry/Entity Type

Business

Requirements
Must have
• Clean, aesthetic and use free stock images

A google map with the office location

```html
<!DOCTYPE html>
<html lang="en">
<head>
<meta charset="utf-8">
<title>Parcel Brisk Couriers</title>
<link rel="stylesheet" href="https://fonts.googleapis.com/css2?family=Roboto+Condensed:wght@300;400;700&family=Open+Sans:wght@400;600&family=Noto+Serif:wght@400;700&display=swap">
<style>
:root{
  --orange:#f04e23;
  --orange-line:#f26a3c;
  --blue:#1a8fd0;
  --blue-btn:#0d9ddb;
  --navy:#1d3d6b;
  --brown:#3a1d0e;
  --tan-light:#d9c095;
  --tan-dark:#a07a45;
  --grey-band:#f1f1f1;
  --grey-text:#666;
  --grey-icon:#a9a9a9;
  --footer:#262626;
  --white:#fff;
}
*{box-sizing:border-box;margin:0;padding:0}
html,body{width:902px;height:1200px;overflow:hidden}
body{position:relative;background:var(--white);font-family:"Open Sans",Arial,sans-serif;color:#333}
.abs{position:absolute}

.top-rule{left:0;top:0;width:902px;height:3px;background:var(--orange-line)}
.site-header{left:0;top:3px;width:902px;height:75px;background:var(--white)}
.brand{left:106px;top:20px;display:flex;align-items:center;gap:8px}
.brand-mark{width:26px;height:26px;border-radius:50%;background:var(--orange)}
.brand-name{font-family:"Roboto Condensed",Arial,sans-serif;font-weight:400;font-size:17px;color:#444;line-height:1}
.main-nav{left:360px;top:28px;display:flex;align-items:center;gap:0}
.main-nav a{font-family:"Roboto Condensed",Arial,sans-serif;font-weight:700;font-size:12px;color:var(--navy);text-decoration:none;padding:5px 10px;margin-right:10px;border-radius:3px;line-height:14px}
.main-nav a.active{background:linear-gradient(#2aa7e6,#0c7fc4);color:var(--white);margin-right:12px}

.hero{left:0;top:78px;width:902px;height:378px;background:radial-gradient(ellipse at 55% 40%,#e3cda4 0%,var(--tan-light) 35%,var(--tan-dark) 100%)}
.hero-figure{left:470px;top:15px;width:240px;height:363px;background:linear-gradient(180deg,rgba(90,90,90,.35),rgba(60,70,90,.45));border-radius:60px 60px 0 0}
.hero-tagline{left:155px;top:141px;width:403px;height:57px;background:var(--brown);clip-path:polygon(2% 0,100% 0,99% 100%,0 100%);font-family:"Roboto Condensed",Arial,sans-serif;font-weight:700;font-size:48px;color:var(--white);line-height:57px;padding-left:12px;letter-spacing:-.5px}
.hero-sub{left:170px;top:288px;font-family:"Roboto Condensed",Arial,sans-serif;font-weight:700;font-size:31px;color:var(--brown);line-height:30px}
.hero-modes{left:169px;top:315px;display:flex;align-items:center;font-family:"Roboto Condensed",Arial,sans-serif;font-weight:700;font-size:36px;line-height:36px}
.hero-modes .air{background:var(--orange);color:var(--white);padding:0 3px}
.hero-modes .amp{color:var(--brown);padding:0 6px}
.hero-modes .road{background:#1c8bc4;color:var(--white);padding:0 3px}
.slider-dots{left:167px;top:429px;display:flex;gap:7px}
.slider-dots span{width:14px;height:14px;background:#5a3410;color:#f3d9a9;font-size:10px;font-family:Arial,sans-serif;text-align:center;line-height:14px}
.slider-dots span.on{background:var(--orange);color:var(--white)}

.services{left:0;top:456px;width:902px;height:187px;background:var(--grey-band)}
.section-title{left:0;width:902px;text-align:center;font-family:"Roboto Condensed",Arial,sans-serif;font-weight:300;color:var(--orange);line-height:1}
.services .section-title{top:17px;font-size:29px}
.title-rule{top:33px;height:1px;background:#e0e0e0}
.service{top:62px;width:236px;height:108px;display:flex;gap:16px}
.service + .service{border-left:1px solid #e2e2e2}
.service-icon{width:34px;height:40px;flex:none;margin-top:11px}
.service-name{font-family:"Roboto Condensed",Arial,sans-serif;font-weight:300;font-size:28px;color:#222;line-height:1;margin-top:14px}
.service-text{font-size:10px;line-height:15px;color:var(--grey-text);margin-top:9px;width:165px}

.welcome .section-title{top:666px;font-size:29px;font-weight:400}
.welcome-lead{left:0;top:704px;width:902px;text-align:center;font-size:12px;color:#222}
.welcome-text{left:140px;top:719px;width:622px;text-align:center;font-size:10.5px;line-height:15px;color:var(--grey-text)}
.welcome-range{left:171px;top:778px;width:560px;font-size:10.5px;color:#111;text-align:justify;text-align-last:justify}
.offer{left:106px;top:803px;width:692px;height:56px}
.offer-main{left:0;top:0;width:462px;height:56px;background:linear-gradient(90deg,#3a84a8 0%,#7a4d87 55%,#b3324a 100%);border-radius:3px 0 0 3px;font-family:"Noto Serif",Georgia,serif;color:var(--white);text-align:center;padding-top:9px}
.offer-main .l1{font-size:14px;line-height:17px}
.offer-main .l2{font-size:17px;line-height:22px}
.offer-free{left:457px;top:-3px;width:235px;height:62px;background:linear-gradient(90deg,#a9542b,#c96d35 50%,#8f3d22);border-radius:0 3px 3px 0;font-family:"Roboto Condensed",Arial,sans-serif;font-weight:700;font-size:23px;color:#f2efe8;text-align:center;line-height:62px;letter-spacing:.5px}

.contact-area{left:0;top:898px;width:902px;height:259px;background:var(--grey-band)}
.block-title{font-family:"Roboto Condensed",Arial,sans-serif;font-weight:400;font-size:18px;color:#444}
.contact-form{left:106px;top:918px;width:176px}
.field{display:block;width:176px;height:23px;margin-top:13px;background:var(--white);border:1px solid #d6d6d6;border-radius:3px;font-size:10px;color:#888;padding:5px 8px}
.contact-form .block-title + .field{margin-top:8px}
.field.message{height:45px;padding-top:27px}
.send{display:inline-block;margin-top:16px;background:var(--blue-btn);color:var(--white);font-size:10px;font-weight:600;padding:4px 7px;border-radius:2px}
.follow{left:371px;top:919px}
.social{left:371px;top:946px;width:38px}
.social-line{left:18px;top:18px;width:2px;height:138px;background:#d8d8d8}
.social-dot{left:0;width:38px;height:38px;border-radius:50%;background:var(--white);border:2px solid #cfcfcf}
.office{left:502px;top:919px}
.map{left:502px;top:950px;width:296px;height:178px;border:3px solid var(--white);background:linear-gradient(135deg,#e6dcc7,#ede5d4 60%,#dfd3bb)}

.site-footer{left:0;top:1157px;width:902px;height:43px;background:var(--footer);text-align:center}
.footer-nav{display:flex;justify-content:center;gap:15px;padding-top:6px}
.footer-nav a{font-size:10px;font-weight:600;color:var(--white);text-decoration:none}
.copyright{font-size:9px;color:var(--white);margin-top:5px}
</style>
</head>
<body>
<div class="abs top-rule"></div>

<header class="abs site-header">
  <div class="abs brand"><span class="brand-mark"></span><span class="brand-name">PARCEL BRISK</span></div>
  <nav class="abs main-nav">
    <a class="active" href="#">Home</a><a href="#">About Us</a><a href="#">Careers</a><a href="#">Contact</a><a href="#">Locations</a><a href="#">Services</a><a href="#">Technology</a>
  </nav>
</header>

<section class="abs hero" role="img" aria-label="Courier holding a cardboard parcel in front of a world map">
  <div class="abs hero-figure"></div>
</section>
<div class="abs hero-tagline">SURE SAFE SWIFT</div>
<div class="abs hero-sub">MOVEMENT BY</div>
<div class="abs hero-modes"><span class="air">AIR RAIL</span><span class="amp">&amp;</span><span class="road">ROAD</span></div>
<div class="abs slider-dots"><span class="on">1</span><span>2</span><span>3</span><span>4</span></div>

<section class="abs services">
  <div class="abs title-rule" style="left:146px;width:240px"></div>
  <div class="abs title-rule" style="left:540px;width:230px"></div>
  <h2 class="abs section-title">SERVICES</h2>

  <div class="abs service" style="left:106px">
    <svg class="service-icon" viewBox="0 0 34 40"><path d="M3 2h19l9 9v27H3z" fill="none" stroke="var(--grey-icon)" stroke-width="3"/><path d="M9 16h16M9 22h16M9 28h12" stroke="var(--grey-icon)" stroke-width="2.5"/></svg>
    <div><div class="service-name">EZY QUOTE</div><p class="service-text">Lorem Ipsum is simply dummy text of the printing and typesetting industry.</p></div>
  </div>
  <div class="abs service" style="left:342px;padding-left:0">
    <svg class="service-icon" viewBox="0 0 34 40"><rect x="0" y="10" width="34" height="22" rx="2" fill="var(--grey-icon)"/><path d="M1 11l16 12 16-12" fill="none" stroke="var(--grey-band)" stroke-width="2.5"/></svg>
    <div><div class="service-name">EZY SEND</div><p class="service-text">Lorem Ipsum is simply dummy text of the printing and typesetting industry.</p></div>
  </div>
  <div class="abs service" style="left:578px">
    <svg class="service-icon" viewBox="0 0 34 40"><path d="M3 2h19l7 7v12M16 38H3V2" fill="none" stroke="var(--grey-icon)" stroke-width="3"/><path d="M8 14h14M8 20h10" stroke="var(--grey-icon)" stroke-width="2.5"/><circle cx="24" cy="28" r="6" fill="none" stroke="var(--grey-icon)" stroke-width="3"/><path d="M28 32l5 6" stroke="var(--grey-icon)" stroke-width="3"/></svg>
    <div><div class="service-name">EZY TRACK</div><p class="service-text">Lorem Ipsum is simply dummy text of the printing and typesetting industry.</p></div>
  </div>
</section>

<section class="welcome">
  <h1 class="abs section-title">WELCOME TO PARCEL BRISK COURIERS</h1>
  <p class="abs welcome-lead">Services is our Sucess</p>
  <p class="abs welcome-text">ParcelSwift is Australia's leading metropolitan express parcel delivery service. With over 550 Contractors nationwide and industry leading technology, ParcelSwift provides unmatched service for your small parcel freight requirements.</p>
  <p class="abs welcome-range">Please check out our full range of services including prepaid coupons, return freight and nationwide satchels.</p>
  <div class="abs offer">
    <div class="abs offer-main"><div class="l1">We also offer our customers the opportunity to manage their</div><div class="l2">freight online</div></div>
    <div class="abs offer-free">FREE OF CHARGE!</div>
  </div>
</section>

<section class="abs contact-area"></section>
<form class="abs contact-form">
  <div class="block-title">Contact</div>
  <div class="field">Your Name</div>
  <div class="field">Your Email</div>
  <div class="field">Subject</div>
  <div class="field message">Your Message</div>
  <span class="send">SEND</span>
</form>
<div class="abs block-title follow">Follow Us</div>
<div class="abs social">
  <div class="abs social-line"></div>
  <div class="abs social-dot" style="top:0" aria-label="Social profile"></div>
  <div class="abs social-dot" style="top:46px" aria-label="Social profile"></div>
  <div class="abs social-dot" style="top:92px" aria-label="Social profile"></div>
  <div class="abs social-dot" style="top:138px" aria-label="Social profile"></div>
</div>
<div class="abs block-title office">Office Location</div>
<div class="abs map" role="img" aria-label="Street map showing the office location"></div>

<footer class="abs site-footer">
  <nav class="footer-nav"><a href="#">Home</a><a href="#">About Us</a><a href="#">Careers</a><a href="#">Contact</a><a href="#">Locations</a><a href="#">Services</a><a href="#">Technology</a></nav>
  <p class="copyright">Copyright © 2013 Parcel Brisk Couriers. All Rights Reserved.</p>
</footer>
</body>
</html>
```